Startup Drone Platform Company business card

We are needing a business card design for our employees. We are a startup drone platform. We are looking for a business card that has our logo on one side, with the employee/company details on the opposite side. We are looking for something that is very eye catching, modern, and bold.

Target Market(s)

This will target both drone pilots and drone businesses, along with all the industries that could utilize drone services (aerial video, aerial photos, inspections, 3d mapping, etc).

Industry/Entity Type

Business

```html
<!DOCTYPE html>
<html lang="en">
<head>
<meta charset="utf-8">
<title>Skylane Aerial – Business Card</title>
<link rel="stylesheet" href="https://fonts.googleapis.com/css2?family=Josefin+Sans:wght@400&family=Lato:wght@300;400&display=swap">
<style>
  :root {
    --canvas: #e9e9e7;
    --card-light: #f4f4f4;
    --card-mid: #d2d2d2;
    --card-shade: #bdbdbd;
    --panel-top: #8d8d8d;
    --panel-bottom: #6c6c6c;
    --panel-edge: #dedede;
    --ink: #1d1d1d;
    --accent: #5cc6cf;
    --contact-text: #ffffff;
    --icon-disc: #141414;
  }
  * { box-sizing: border-box; margin: 0; padding: 0; }
  html, body {
    width: 1200px;
    height: 675px;
    overflow: hidden;
    background: var(--canvas);
  }
  .canvas {
    position: relative;
    width: 1200px;
    height: 675px;
  }
  .card {
    position: absolute;
    top: 182px;
    width: 540px;
    height: 310px;
    background: linear-gradient(160deg, var(--card-light) 0%, var(--card-mid) 70%, var(--card-shade) 100%);
    box-shadow: 0 10px 26px rgba(0,0,0,0.18);
    overflow: hidden;
  }
  .card--front { left: 40px; }
  .card--back { left: 620px; }

  .wordmark {
    display: flex;
    align-items: center;
    gap: 14px;
  }
  .wordmark__dot {
    width: 16px;
    height: 16px;
    border-radius: 50%;
    background: var(--accent);
    flex: none;
  }
  .wordmark__name {
    font-family: "Josefin Sans", sans-serif;
    font-weight: 400;
    color: var(--ink);
    letter-spacing: 0.32em;
    line-height: 1.25;
    text-transform: uppercase;
  }
  .card--front .wordmark {
    position: absolute;
    left: 0; right: 0; top: 0; bottom: 0;
    justify-content: center;
  }
  .card--front .wordmark__name { font-size: 30px; }

  .card__panel {
    position: absolute;
    inset: 0;
  }
  .card--back .wordmark {
    position: absolute;
    left: 44px;
    top: 128px;
  }
  .card--back .wordmark__name { font-size: 24px; }

  .contact-list {
    position: absolute;
    left: 350px;
    top: 64px;
    list-style: none;
    display: flex;
    flex-direction: column;
    gap: 22px;
  }
  .contact-item {
    display: flex;
    align-items: center;
    gap: 10px;
  }
  .contact-item__icon {
    width: 28px;
    height: 28px;
    border-radius: 50%;
    background: var(--icon-disc);
    display: flex;
    align-items: center;
    justify-content: center;
    flex: none;
  }
  .contact-item__text {
    font-family: "Lato", sans-serif;
    font-weight: 300;
    font-size: 12px;
    line-height: 1.35;
    color: var(--contact-text);
    white-space: nowrap;
  }
</style>
</head>
<body>
<main class="canvas">

  <section class="card card--front" aria-label="Business card, logo side">
    <div class="wordmark">
      <span class="wordmark__dot"></span>
      <span class="wordmark__name">Skylane<br>Aerial</span>
    </div>
  </section>

  <section class="card card--back" aria-label="Business card, contact side">
    <svg class="card__panel" width="540" height="310" viewBox="0 0 540 310" aria-hidden="true">
      <defs>
        <linearGradient id="panelFill" x1="0" y1="0" x2="0" y2="1">
          <stop offset="0" stop-color="var(--panel-top)"/>
          <stop offset="1" stop-color="var(--panel-bottom)"/>
        </linearGradient>
      </defs>
      <path d="M300 0 C266 110 278 220 330 310 L540 310 L540 0 Z" fill="var(--panel-edge)"/>
      <path d="M320 0 C288 110 300 220 350 310 L540 310 L540 0 Z" fill="url(#panelFill)"/>
    </svg>

    <div class="wordmark">
      <span class="wordmark__dot"></span>
      <span class="wordmark__name">Skylane<br>Aerial</span>
    </div>

    <ul class="contact-list">
      <li class="contact-item">
        <span class="contact-item__icon">
          <svg width="14" height="14" viewBox="0 0 24 24" aria-hidden="true">
            <path fill="#fff" d="M6.6 10.8a15.1 15.1 0 0 0 6.6 6.6l2.2-2.2a1 1 0 0 1 1-.25 11.4 11.4 0 0 0 3.6.57 1 1 0 0 1 1 1V20a1 1 0 0 1-1 1A17 17 0 0 1 3 4a1 1 0 0 1 1-1h3.5a1 1 0 0 1 1 1c0 1.250.2 2.450.57 3.570a1 1 0 0 1-.25 1z"/>
          </svg>
        </span>
        <span class="contact-item__text">+1 234 567 8910<br>+1 234 567 8910</span>
      </li>
      <li class="contact-item">
        <span class="contact-item__icon">
          <svg width="14" height="14" viewBox="0 0 24 24" aria-hidden="true">
            <rect x="3" y="5" width="18" height="14" rx="1.5" fill="none" stroke="#fff" stroke-width="2"/>
            <path d="M3.5 6l8.5 7 8.5-7" fill="none" stroke="#fff" stroke-width="2"/>
          </svg>
        </span>
        <span class="contact-item__text">your@e-mail.com<br>www.yourwebsite.com</span>
      </li>
      <li class="contact-item">
        <span class="contact-item__icon">
          <svg width="14" height="14" viewBox="0 0 24 24" aria-hidden="true">
            <path fill="#fff" d="M12 2a7 7 0 0 0-7 7c0 5.2 7 13 7 13s7-7.8 7-13a7 7 0 0 0-7-7zm0 9.5A2.5 2.5 0 1 1 12 6.5a2.5 2.5 0 0 1 0 5z"/>
          </svg>
        </span>
        <span class="contact-item__text">Your Street name, City,<br>Country, Zip Code.</span>
      </li>
    </ul>
  </section>

</main>
</body>
</html>
```